Realtor branding business card

modern, simple and self branding. Broker office logo needs to be used but not emphasized. Looking to brand myself

Target Market(s)

buyers, sellers and investors

Industry/Entity Type

Realtor

Contact Information for Business Card

Sample of my current business card on file

Requirements
Must have
• my website - emilioverdaskt.com
• Realtor logo
• Fair housing logo
Nice to have
• Colors from office logo but not a must
Should not have
• Do not want headshot

```html
<!DOCTYPE html>
<html lang="en">
<head>
<meta charset="utf-8">
<title>Emilio Verdas – Business Card</title>
<link href="https://fonts.googleapis.com/css2?family=Montserrat:wght@400;500;700;800&display=swap" rel="stylesheet">
<style>
  :root {
    --navy: #2a2a72;
    --red: #d9272a;
    --ink: #222222;
    --muted: #555555;
    --rule: #d4d4d4;
    --skyline: #d9d9d9;
    --card: #ffffff;
    --backdrop: #2f2f2f;
  }
  * { margin: 0; padding: 0; box-sizing: border-box; }
  html, body { width: 1200px; height: 1200px; overflow: hidden; }
  body {
    background: var(--backdrop);
    font-family: "Montserrat", sans-serif;
    position: relative;
  }
  .card {
    position: absolute;
    width: 730px;
    height: 416px;
    background: var(--card);
    overflow: hidden;
  }
  .card--front { left: 235px; top: 105px; }
  .card--back  { left: 234px; top: 670px; }

  .skyline {
    position: absolute;
    bottom: 0;
    background: linear-gradient(to top, var(--skyline) 0%, rgba(217,217,217,0.75) 55%, rgba(217,217,217,0) 100%);
  }
  .card--front .skyline { left: 0; width: 730px; height: 140px; }
  .card--back .skyline { left: 390px; width: 342px; height: 150px; }

  .brand {
    position: absolute;
    color: var(--navy);
    font-weight: 800;
    line-height: 1;
    text-align: left;
  }
  .brand__name { display: block; }
  .brand__sub { display: block; }
  .brand__mark {
    position: absolute;
    background: var(--red);
  }
  .card--front .brand { left: 220px; top: 150px; }
  .card--front .brand__name { font-size: 54px; letter-spacing: -1px; }
  .card--front .brand__sub { font-size: 28px; margin-top: 6px; letter-spacing: 0.5px; }
  .card--front .brand__mark { width: 18px; height: 18px; left: -32px; top: 6px; }

  .card--back .brand { left: 44px; top: 170px; }
  .card--back .brand__name { font-size: 42px; letter-spacing: -1px; }
  .card--back .brand__sub { font-size: 22px; margin-top: 5px; letter-spacing: 0.4px; }
  .card--back .brand__mark { width: 14px; height: 14px; left: -24px; top: 5px; display: none; }

  .corner { position: absolute; }
  .corner--top { left: 0; top: 0; }
  .corner--bottom { right: 0; bottom: 0; }

  .divider {
    position: absolute;
    left: 326px;
    top: 82px;
    width: 2px;
    height: 252px;
    background: var(--rule);
  }
  .agent {
    position: absolute;
    left: 369px;
    top: 86px;
  }
  .agent__name {
    font-size: 27px;
    font-weight: 700;
    color: var(--navy);
    letter-spacing: 0.3px;
  }
  .agent__title {
    font-size: 18px;
    font-weight: 500;
    color: var(--muted);
    margin-top: 6px;
  }
  .contact {
    position: absolute;
    left: 369px;
    top: 176px;
    list-style: none;
  }
  .contact__item {
    display: flex;
    align-items: center;
    font-size: 18px;
    color: var(--ink);
    height: 24px;
    margin-bottom: 16px;
  }
  .contact__icon { width: 16px; height: 16px; margin-right: 12px; }
  .badges {
    position: absolute;
    left: 369px;
    top: 290px;
    display: flex;
    gap: 20px;
  }
  .badge { width: 40px; height: 44px; }
</style>
</head>
<body>

<section class="card card--front">
  <div class="skyline" role="img" aria-label="Pale grey city skyline silhouette along the bottom of the card"></div>
  <div class="brand">
    <span class="brand__mark"></span>
    <span class="brand__name">Northgate</span>
    <span class="brand__sub">Realty Group</span>
  </div>
</section>

<section class="card card--back">
  <svg class="corner corner--top" width="50" height="62" viewBox="0 0 50 62"><polygon points="0,0 50,0 0,62" fill="var(--red)"/></svg>
  <div class="skyline" role="img" aria-label="Pale grey city skyline silhouette in the lower right corner"></div>
  <svg class="corner corner--bottom" width="56" height="72" viewBox="0 0 56 72"><polygon points="56,0 56,72 0,72" fill="var(--navy)"/></svg>

  <div class="brand">
    <span class="brand__mark"></span>
    <span class="brand__name">Northgate</span>
    <span class="brand__sub">Realty Group</span>
  </div>

  <div class="divider"></div>

  <div class="agent">
    <h1 class="agent__name">EMILIO VERDAS</h1>
    <p class="agent__title">PA Realtor</p>
  </div>

  <ul class="contact">
    <li class="contact__item">
      <svg class="contact__icon" viewBox="0 0 16 16" fill="none" stroke="#9a9a9a" stroke-width="1.1">
        <circle cx="8" cy="8" r="6.5"/><ellipse cx="8" cy="8" rx="3" ry="6.5"/><line x1="1.5" y1="8" x2="14.5" y2="8"/><line x1="2.5" y1="4.5" x2="13.5" y2="4.5"/><line x1="2.5" y1="11.5" x2="13.5" y2="11.5"/>
      </svg>
      emilioverdaskt.com
    </li>
    <li class="contact__item">
      <svg class="contact__icon" viewBox="0 0 16 16" fill="none" stroke="#9a9a9a" stroke-width="1.1">
        <rect x="1" y="3" width="14" height="10"/><polyline points="1,3 8,9 15,3"/>
      </svg>
      Verdasrealty@mailbox.com
    </li>
  </ul>

  <div class="badges">
    <svg class="badge" viewBox="0 0 40 44" role="img" aria-label="Realtor membership badge"><rect x="2" y="2" width="36" height="34" fill="#6b6b6b"/></svg>
    <svg class="badge" viewBox="0 0 40 44" role="img" aria-label="Fair housing badge"><polygon points="20,2 38,16 38,36 2,36 2,16" fill="#6b6b6b"/></svg>
  </div>
</section>

</body>
</html>
```